Vesk Architecture

We are a architectural design and build company working between scales 1/1000 to 1/1 we want people to understand our difference from our design experience and quality.we build hotels restourants and office spaces.Our company name is Vesk architecture to mind sustainability.

We want to write our adress phone and work spesifications on the card and we want our logo as backround.

Ps:you could find the logo adress and phone box numbers from the web:www.veskmimarlik-ornek.com

Target Market(s)

Who looks for experts.

Industry/Entity Type

Architecture

Requirements
Must have
• Design is over everything.
Should not have
• we don want it to be colorfull

```html
<!DOCTYPE html>
<html lang="tr">
<head>
<meta charset="utf-8">
<title>Vesk Mimarlık – Kartvizit</title>
<link href="https://fonts.googleapis.com/css2?family=Barlow:wght@400;500&display=swap" rel="stylesheet">
<style>
  :root {
    --backdrop: #d6d6d6;
    --card-white: #ffffff;
    --ink: #141414;
    --ink-soft: #3a3a3a;
    --divider: #c9c9c9;
    --slate-light: #8c8c8c;
    --slate-dark: #3b3b3b;
    --slate-centre: #8a8a8a;
    --slate-edge: #363636;
    --paper-text: #e4e4e4;
  }
  * { margin: 0; padding: 0; box-sizing: border-box; }
  html, body {
    width: 1200px;
    height: 900px;
    overflow: hidden;
    background: var(--backdrop);
    font-family: "Barlow", sans-serif;
  }
  .card {
    position: absolute;
    top: 111px;
    width: 400px;
    height: 619px;
    overflow: hidden;
  }
  .card--front { left: 144px; background: var(--card-white); }
  .card--back {
    left: 657px;
    background: radial-gradient(ellipse at 50% 45%, var(--slate-centre) 0%, #5e5e5e 45%, var(--slate-edge) 100%);
  }
  .brand-name {
    position: absolute;
    left: 0;
    right: 0;
    text-align: center;
    font-weight: 500;
    letter-spacing: 0.04em;
    line-height: 1.2;
  }
  .card--front .brand-name {
    top: 72px;
    font-size: 42px;
    color: var(--ink);
  }
  .card--back .brand-name {
    top: 276px;
    font-size: 54px;
    color: var(--card-white);
  }
  .holder {
    position: absolute;
    top: 337px;
    left: 0;
    right: 0;
    text-align: center;
    color: var(--ink-soft);
  }
  .holder__name { font-size: 19px; line-height: 23px; letter-spacing: 0.03em; }
  .holder__role { font-size: 14px; line-height: 17px; margin-top: 5px; letter-spacing: 0.03em; }
  .divider {
    position: absolute;
    top: 399px;
    left: 0;
    width: 100%;
    height: 12px;
    background: linear-gradient(to bottom, #ededed 0%, var(--divider) 60%, #a8a8a8 100%);
  }
  .contact-panel {
    position: absolute;
    top: 411px;
    left: 0;
    width: 100%;
    bottom: 0;
    background: linear-gradient(to bottom, var(--slate-light) 0%, #6a6a6a 45%, var(--slate-dark) 100%);
  }
  .contact {
    position: absolute;
    top: 47px;
    left: 56px;
    list-style: none;
    color: var(--paper-text);
    font-size: 16px;
    line-height: 21.5px;
    letter-spacing: 0.02em;
  }
  .contact__label { display: inline-block; width: 20px; }
</style>
</head>
<body>
  <section class="card card--front">
    <div class="brand-name">Vesk Mimarlık</div>
    <div class="holder">
      <p class="holder__name">Deniz Arman KAYA</p>
      <p class="holder__role">Mimar</p>
    </div>
    <div class="divider"></div>
    <div class="contact-panel">
      <ul class="contact">
        <li>Yeldeğirmeni Mah. Rıhtım Cad. Ayva Sok.</li>
        <li>No:7 Kadıköy / İSTANBUL</li>
        <li><span class="contact__label">t.</span>0216 555 01 47</li>
        <li><span class="contact__label">f.</span>0216 555 01 48</li>
        <li><span class="contact__label">e.</span>veskmimarlik@ornek-posta.com</li>
      </ul>
    </div>
  </section>

  <section class="card card--back">
    <div class="brand-name">Vesk Mimarlık</div>
  </section>
</body>
</html>
```